Redesign my business cards

I would like pretty much all the same information as my current business cards but redesigned to stand out more and be more unique photo uploaded to show my current business cards don’t mind if you want to remove or replace I for on the back

```html
<!DOCTYPE html>
<html lang="en">
<head>
<meta charset="utf-8">
<title>Halvern Detailing – Business Cards</title>
<link rel="stylesheet" href="https://fonts.googleapis.com/css2?family=Montserrat:wght@400;500&family=Oswald:wght@400;500&display=swap">
<style>
  :root {
    --backdrop: #3a3a3c;
    --card: #062a3d;
    --card-deep: #04202f;
    --blue: #3a7fd8;
    --cyan: #4ccfe8;
    --accent: #4a9be6;
    --brand: #8a4fe0;
    --white: #f3f6f8;
    --muted: #c9d6de;
  }
  * { box-sizing: border-box; margin: 0; padding: 0; }
  html, body { width: 1200px; height: 1200px; overflow: hidden; }
  body { background: var(--backdrop); position: relative; font-family: "Oswald", sans-serif; }

  .card {
    position: absolute; left: 220px; width: 760px; height: 463px;
    background: linear-gradient(135deg, var(--card) 0%, #0a3347 55%, var(--card-deep) 100%);
    border-radius: 34px; overflow: hidden;
    box-shadow: 0 18px 40px rgba(0,0,0,.45);
  }
  .card--front { top: 80px; }
  .card--back { top: 640px; }

  .wave { position: absolute; inset: 0; width: 100%; height: 100%; }

  .brand-mark { position: absolute; display: flex; flex-direction: column; align-items: center; gap: 18px; }
  .card--front .brand-mark { left: 60px; top: 110px; width: 260px; }
  .card--back .brand-mark { right: 50px; top: 110px; width: 260px; }
  .brand-mark__dot { width: 110px; height: 110px; border-radius: 50%; background: var(--accent); }
  .brand-mark__name { font-family: "Oswald", sans-serif; font-weight: 500; font-size: 30px; letter-spacing: 5px; color: var(--brand); text-transform: uppercase; text-align: center; line-height: 1.15; }

  .contact { position: absolute; left: 400px; top: 78px; }
  .contact__name { font-family: "Montserrat", sans-serif; font-weight: 500; font-size: 34px; color: var(--accent); letter-spacing: .5px; line-height: 1; }
  .contact__role { font-family: "Montserrat", sans-serif; font-weight: 400; font-size: 17px; color: var(--white); letter-spacing: 1px; margin-top: 4px; }
  .contact__list { list-style: none; margin-top: 18px; }
  .contact__item { display: flex; align-items: center; gap: 10px; font-size: 20px; color: var(--white); text-transform: uppercase; margin-bottom: 6px; }
  .contact__icon { width: 20px; height: 20px; flex: none; }

  .services { position: absolute; left: 48px; top: 60px; width: 430px; }
  .service { margin-bottom: 26px; }
  .service__head { display: flex; align-items: flex-end; gap: 10px; }
  .service__title { font-size: 25px; font-weight: 500; color: var(--blue); text-transform: uppercase; white-space: nowrap; line-height: 1; }
  .service__rule { flex: 1; height: 1px; background: var(--accent); margin-bottom: 6px; }
  .service__price { font-size: 26px; font-weight: 500; color: var(--accent); line-height: 1; }
  .service__desc { font-size: 14px; color: var(--white); text-transform: uppercase; line-height: 1.3; margin-top: 6px; letter-spacing: .2px; }
</style>
</head>
<body>

<section class="card card--front" aria-label="Business card front">
  <svg class="wave" viewBox="0 0 760 463" preserveAspectRatio="none" aria-hidden="true">
    <defs>
      <linearGradient id="bandFill" x1="0" y1="1" x2="1" y2="0">
        <stop offset="0" stop-color="#3a7fd8"/>
        <stop offset="1" stop-color="#4ccfe8"/>
      </linearGradient>
    </defs>
    <path d="M170 463 C 240 360, 430 360, 560 320 C 680 284, 735 230, 760 170 L760 463 Z" fill="url(#bandFill)"/>
    <path d="M190 463 C 260 372, 440 372, 568 332 C 684 296, 738 244, 760 190 L760 205 C 740 258, 688 312, 574 346 C 448 384, 276 384, 208 463 Z" fill="#062a3d"/>
    <path d="M240 463 C 320 405, 470 400, 600 360 C 700 330, 745 290, 760 250 L760 463 Z" fill="#062a3d"/>
  </svg>

  <div class="brand-mark">
    <span class="brand-mark__dot"></span>
    <span class="brand-mark__name">Halvern<br>Detailing</span>
  </div>

  <div class="contact">
    <h1 class="contact__name">OWEN MARLOWE</h1>
    <p class="contact__role">OWNER | OPERATOR</p>
    <ul class="contact__list">
      <li class="contact__item">
        <svg class="contact__icon" viewBox="0 0 24 24" aria-hidden="true"><path fill="#4a9be6" d="M6.6 10.8a15.1 15.1 0 0 0 6.6 6.6l2.2-2.2a1 1 0 0 1 1-.25 11.4 11.4 0 0 0 3.6.57 1 1 0 0 1 1 1V20a1 1 0 0 1-1 1A17 17 0 0 1 3 4a1 1 0 0 1 1-1h3.5a1 1 0 0 1 1 1c0 1.25.2 2.45.57 3.57a1 1 0 0 1-.25 1z"/></svg>
        0412 557 019
      </li>
      <li class="contact__item">
        <svg class="contact__icon" viewBox="0 0 24 24" aria-hidden="true"><rect x="2" y="5" width="20" height="14" rx="1" fill="#4a9be6"/><path d="M2 6l10 7 10-7" fill="none" stroke="#062a3d" stroke-width="1.6"/></svg>
        halverndetailing@mailbox.com
      </li>
    </ul>
  </div>
</section>

<section class="card card--back" aria-label="Business card back">
  <div class="services">
    <article class="service">
      <div class="service__head"><h2 class="service__title">Interior Detail</h2><span class="service__rule"></span><span class="service__price">$150</span></div>
      <p class="service__desc">Vacume &amp; deep clean of carpets &amp; upholstery or leather treatment, interior trim clean &amp; condition, window polish and treatment, steam clean and stain removal</p>
    </article>
    <article class="service">
      <div class="service__head"><h2 class="service__title">Exterior Detail</h2><span class="service__rule"></span><span class="service__price">$250</span></div>
      <p class="service__desc">Extreme wash &amp; polish, exterior trim reviver &amp; protector window polish &amp; treatment, tyre dressing, engine bay cleaned</p>
    </article>
    <article class="service">
      <div class="service__head"><h2 class="service__title">Full Extreme Detail</h2><span class="service__rule"></span><span class="service__price">$350</span></div>
      <p class="service__desc">Vacume &amp; deep clean of carpets &amp; upholstery or leather treatment, interior trim clean &amp; condition, window polish and treatment, steam clean and stain removal</p>
    </article>
  </div>

  <div class="brand-mark">
    <span class="brand-mark__dot"></span>
    <span class="brand-mark__name">Halvern<br>Detailing</span>
  </div>
</section>

</body>
</html>
```